RZ Advisory Business Cards - High End AV / Low Voltage Company

We are low voltage AV company that specializes in high end clients on the residential side and larger businesses on the commercial side. We want something modern, tech looking but also something that is extremely professional looking. We have uploaded our logos and postcards we already have in the field. Along with a picture of one of our wrapped vans. Our website is at www.rzadvisory.example and our primary colors are the orange, green, grey and blue all military color finishes.

We are interesting in the slogans "Matching You with the Ideal Equipment" or "Guiding the Harborlands in Tech"

Target Market(s)

We focus on 70% Commercial and 30% Residential Customers

Industry/Entity Type

Low Voltage, AV Company

Contact Information for Business Card

Name - Dorian Fenwick, Title - Owner, Office Phone - 555-402-7163, Mobile Phone - 555-718-3094, E-Mail - t@rzadvisory.example, Website: www.rzadvisory.example

Font styles to use
Sans Serif

Requirements
Must have
• Must have Name, Title, Work Phone & Mobile, Website and Logo.
Nice to have
• We want something that will impress our higher end clients with a great logo
Should not have
• Too traditional or plain.

```html
<!DOCTYPE html>
<html lang="en">
<head>
<meta charset="utf-8">
<title>RZ Advisory Business Cards</title>
<link href="https://fonts.googleapis.com/css2?family=Montserrat:wght@500;600;700&family=Lato:wght@400;700&display=swap" rel="stylesheet">
<style>
  :root {
    --bg: #2b2b2b;
    --olive: #4b5235;
    --olive-dark: #2a3020;
    --orange: #e8683a;
    --white: #ffffff;
    --ink: #1f2418;
    --rule: #3a3a3a;
  }
  * { box-sizing: border-box; margin: 0; padding: 0; }
  html, body { width: 1200px; height: 694px; overflow: hidden; background: var(--bg); }
  .stage { position: relative; width: 1200px; height: 694px; }
  .card {
    position: absolute; top: 192px; width: 540px; height: 309px;
    border-radius: 26px; overflow: hidden;
  }
  .card-front { left: 40px; background: var(--olive); }
  .card-back { left: 620px; background: var(--white); }

  /* Brand lockup */
  .brand { display: flex; align-items: center; gap: 12px; }
  .brand-dot { border-radius: 50%; background: var(--orange); flex: none; }
  .brand-name {
    font-family: "Montserrat", sans-serif; font-weight: 700;
    color: var(--orange); letter-spacing: 0.04em; text-transform: uppercase; white-space: nowrap;
  }

  .card-front .front-content {
    position: absolute; inset: 0; display: flex; flex-direction: column;
    align-items: center; justify-content: center; gap: 22px;
  }
  .card-front .brand-dot { width: 30px; height: 30px; }
  .card-front .brand-name { font-size: 40px; }
  .slogan {
    font-family: "Lato", sans-serif; font-weight: 700; color: var(--white);
    font-size: 17px; letter-spacing: 0.02em;
  }

  /* Back card */
  .back-left { position: absolute; left: 30px; top: 30px; width: 250px; }
  .card-back .brand-dot { width: 20px; height: 20px; }
  .card-back .brand-name { font-size: 25px; }
  .person-name {
    margin-top: 46px; font-family: "Montserrat", sans-serif; font-weight: 700;
    font-size: 27px; color: var(--ink);
  }
  .person-title {
    margin-top: 4px; font-family: "Montserrat", sans-serif; font-weight: 500;
    font-size: 16px; color: var(--ink);
  }
  .rule { height: 1px; background: var(--rule); }
  .back-left .rule { margin: 12px 0 12px; width: 200px; }
  .contact-list { list-style: none; display: flex; flex-direction: column; gap: 7px; }
  .contact-item {
    display: flex; align-items: center; gap: 10px;
    font-family: "Montserrat", sans-serif; font-weight: 500; font-size: 16px; color: var(--ink);
  }
  .contact-item svg { width: 16px; height: 16px; flex: none; fill: var(--orange); }

  .back-right { position: absolute; right: 26px; top: 26px; width: 232px; }
  .van-photo {
    width: 232px; height: 150px; border-radius: 14px;
    background: linear-gradient(160deg, #5d6a3c 0%, #46512b 55%, #2e3520 100%);
  }
  .back-right .rule { margin: 16px 0 14px; }
  .back-right .contact-list { align-items: flex-start; }
  .back-right .contact-item { font-size: 14px; }
</style>
</head>
<body>
<main class="stage">
  <section class="card card-front" aria-label="Business card front">
    <div class="front-content">
      <div class="brand">
        <span class="brand-dot"></span>
        <span class="brand-name">RZ Advisory</span>
      </div>
      <p class="slogan">Matching You with the Ideal Equipment</p>
    </div>
  </section>

  <section class="card card-back" aria-label="Business card back">
    <div class="back-left">
      <div class="brand">
        <span class="brand-dot"></span>
        <span class="brand-name">RZ Advisory</span>
      </div>
      <h1 class="person-name">Dorian Fenwick</h1>
      <p class="person-title">Owner</p>
      <div class="rule"></div>
      <ul class="contact-list">
        <li class="contact-item">
          <svg viewBox="0 0 24 24" aria-hidden="true"><path d="M6.6 10.8a15.1 15.1 0 0 0 6.6 6.6l2.2-2.2a1 1 0 0 1 1-.25 11.4 11.4 0 0 0 3.6.57 1 1 0 0 1 1 1V20a1 1 0 0 1-1 1A17 17 0 0 1 3 4a1 1 0 0 1 1-1h3.5a1 1 0 0 1 1 1c0 1.25.2 2.45.57 3.57a1 1 0 0 1-.25 1z"/></svg>
          555-402-7163
        </li>
        <li class="contact-item">
          <svg viewBox="0 0 24 24" aria-hidden="true"><path d="M7 1h10a2 2 0 0 1 2 2v18a2 2 0 0 1-2 2H7a2 2 0 0 1-2-2V3a2 2 0 0 1 2-2zm0 3v14h10V4zm5 15.2a1.2 1.2 0 1 0 0 2.4 1.2 1.2 0 0 0 0-2.4z"/></svg>
          555-718-3094
        </li>
      </ul>
    </div>

    <div class="back-right">
      <div class="van-photo" role="img" aria-label="Photo of the company's olive green wrapped service van with a ladder on the roof rack"></div>
      <div class="rule"></div>
      <ul class="contact-list">
        <li class="contact-item">
          <svg viewBox="0 0 24 24" aria-hidden="true"><path d="M2 5h20v14H2zm2 2v.5l8 5 8-5V7zm0 2.9V17h16V9.9l-8 5z"/></svg>
          t@rzadvisory.example
        </li>
        <li class="contact-item">
          <svg viewBox="0 0 24 24" aria-hidden="true"><path d="M12 2a10 10 0 1 0 0 20 10 10 0 0 0 0-20zm6.9 9h-3a15 15 0 0 0-1.3-5.6A8 8 0 0 1 18.9 11zM12 4.1c.9 1.2 1.8 3.6 1.9 6.9h-3.8c.1-3.3 1-5.7 1.9-6.9zM9.4 5.4A15 15 0 0 0 8.1 11h-3a8 8 0 0 1 4.3-5.6zM5.1 13h3a15 15 0 0 0 1.3 5.6A8 8 0 0 1 5.1 13zm6.9 6.9c-.9-1.2-1.8-3.6-1.9-6.9h3.8c-.1 3.3-1 5.7-1.9 6.9zm2.6-1.3a15 15 0 0 0 1.3-5.6h3a8 8 0 0 1-4.3 5.6z"/></svg>
          www.rzadvisory.example
        </li>
      </ul>
    </div>
  </section>
</main>
</body>
</html>
```